Talent Management Company Needs Business Cards

Using one of the logos provided (attached) K&K Talent Collective needs a business card designed.
Please visit our website for more information about us-

www.kktalentcollective.net

The face should feature a dramatic presentation of the logo with the back being reserved for our professional information which is:

The information should be:
Darnell T. Fosbury
C.E.O
Email: dtfosbury@kktalentcollective.net
Mobile: 216-555-0193
Website: www.kktalentcollective.net

Marcus L. Fosbury
Director of Public Relations
Email: mlfosbury@kktalentcollective.net
Mobile: 216-555-0147

Rory J. Whitcomb
Director of Client Development
Email: rwhitcomb@kktalentcollective.net

Glenn Strauss
Director of Brand Development
Email: gstrauss@kktalentcollective.net

Would like the logo to have color. I would like to see one side red or black and the other side white but if it looks better in either black or red that would be fine to but would like to see how it comes out.

Please feel free to message me and if you would like just the icon alone I have other image files that I can send as well.

Target Market(s)

Professional Athletes, coaches, entertainers age 18-35 but also must be accepted in the business community

Industry/Entity Type

Business

Requirements
Must have
• 1) Use the logo
2) Double sided
3) Distinctive
Nice to have
• Small simple images for telephone, e-mail, and Url.

```html
<!DOCTYPE html>
<html lang="en">
<head>
<meta charset="utf-8">
<title>K&amp;K Talent Collective — Business Cards</title>
<link href="https://fonts.googleapis.com/css2?family=Didact+Gothic&display=swap" rel="stylesheet">
<style>
  :root {
    --canvas-bg: #1c1c1c;
    --card-black: #050505;
    --card-black-edge: #151515;
    --card-red-light: #8e0a0a;
    --card-red-dark: #4f0000;
    --accent-red: #d4151c;
    --ink-white: #f2f2f2;
    --ink-dark: #120000;
    --strip-white: #f4f4f4;
  }
  * { margin: 0; padding: 0; box-sizing: border-box; }
  html, body {
    width: 1200px; height: 900px; overflow: hidden;
    background: var(--canvas-bg);
    font-family: "Didact Gothic", "Century Gothic", sans-serif;
  }
  .canvas { position: relative; width: 1200px; height: 900px; }

  .card { position: absolute; width: 620px; height: 370px; }

  .card-front {
    left: 110px; top: 100px;
    background: radial-gradient(ellipse at 50% 35%, var(--card-black-edge), var(--card-black) 70%);
    display: flex; flex-direction: column; align-items: center; justify-content: center; gap: 18px;
  }
  .brand-dot {
    width: 70px; height: 70px; border-radius: 50%;
    background: var(--accent-red);
  }
  .brand-name {
    color: var(--ink-white);
    font-size: 30px; letter-spacing: 1px; text-transform: uppercase;
  }

  .card-back {
    left: 480px; top: 470px;
    background: linear-gradient(135deg, var(--card-red-light), var(--card-red-dark));
    border-top: 14px solid var(--strip-white);
    border-bottom: 14px solid var(--strip-white);
    display: flex; align-items: center;
  }
  .back-mark {
    flex: 0 0 250px; display: flex; justify-content: center;
  }
  .back-mark .brand-dot { width: 150px; height: 150px; background: var(--ink-white); opacity: 0.85; }
  .contact-list {
    list-style: none; color: var(--ink-dark);
    font-size: 13px; line-height: 1.2;
    display: flex; flex-direction: column; gap: 12px;
  }
  .contact-name, .contact-title { font-size: 15px; }
</style>
</head>
<body>
<main class="canvas">
  <section class="card card-front" aria-label="Card front">
    <div class="brand-dot"></div>
    <div class="brand-name">K&amp;K Talent Collective</div>
  </section>

  <section class="card card-back" aria-label="Card back">
    <div class="back-mark"><div class="brand-dot"></div></div>
    <ul class="contact-list">
      <li>
        <div class="contact-name">Darnell T. Fosbury</div>
        <div class="contact-title">C.E.O</div>
        <div>Email: dtfosbury@kktalentcollective.net</div>
        <div>Mobile: 216-555-0193</div>
        <div>Website: www.kktalentcollective.net</div>
      </li>
      <li>
        <div class="contact-name">Marcus L. Fosbury</div>
        <div class="contact-title">Director of Public Relations</div>
        <div>Email: mlfosbury@kktalentcollective.net</div>
        <div>Mobile: 216-555-0147</div>
        <div>Website: www.kktalentcollective.net</div>
      </li>
      <li>
        <div class="contact-name">Rory J. Whitcomb</div>
        <div class="contact-title">Director of Client Development</div>
        <div>Email: rwhitcomb@kktalentcollective.net</div>
        <div>Website: www.kktalentcollective.net</div>
      </li>
      <li>
        <div class="contact-name">Glenn Strauss</div>
        <div class="contact-title">Director of Brand Development</div>
        <div>Email: gstrauss@kktalentcollective.net</div>
        <div>Website: www.kktalentcollective.net</div>
      </li>
    </ul>
  </section>
</main>
</body>
</html>
```